Larkmoor Business Card Design Project

Double side card , just the logo on oxford white background on one side , and the rest of the information on the other side..
the company name is : Larkmoor Continental General Trading LLC.
logo is already attached
the card to show in the info side: company name, employee name and position (job title) phone number, fax number, email address, P.O. box, Location (city and country)
deadline is already extended 4 all to have more time... thanks

```html
<!DOCTYPE html>
<html lang="en">
<head>
<meta charset="utf-8">
<title>Larkmoor Business Card</title>
<link rel="stylesheet" href="https://fonts.googleapis.com/css2?family=Open+Sans:wght@400;600;700&display=swap">
<style>
  :root {
    --backdrop: #e9eaec;
    --oxford-white: #fbfbfa;
    --brand-blue: #0a3f8c;
    --name-blue: #1752a8;
    --ink: #2b2b2e;
    --ink-soft: #4a4a4f;
    --logo-grey: #3a3b40;
    --card-shadow: 0 6px 18px rgba(0, 0, 0, 0.12);
  }
  * { box-sizing: border-box; margin: 0; padding: 0; }
  html, body {
    width: 1200px;
    height: 800px;
    overflow: hidden;
  }
  body {
    background: var(--backdrop);
    font-family: "Open Sans", Arial, sans-serif;
    display: flex;
    align-items: center;
    justify-content: center;
    gap: 60px;
  }
  .card {
    width: 520px;
    height: 297px;
    background: var(--oxford-white);
    box-shadow: var(--card-shadow);
    position: relative;
    overflow: hidden;
  }

  /* Info side */
  .card--info { display: flex; }
  .info__band {
    width: 46%;
    background: var(--brand-blue);
    display: flex;
    align-items: flex-end;
    padding: 0 26px 30px;
  }
  .info__company {
    color: #ffffff;
    font-size: 17px;
    font-weight: 400;
    line-height: 1.25;
    letter-spacing: 0.2px;
  }
  .info__details {
    flex: 1;
    display: flex;
    flex-direction: column;
    justify-content: space-between;
    align-items: flex-end;
    text-align: right;
    padding: 34px 26px 30px 20px;
  }
  .person__name {
    color: var(--name-blue);
    font-size: 17px;
    font-weight: 600;
    line-height: 1.2;
  }
  .person__position {
    color: var(--ink);
    font-size: 15px;
    font-weight: 600;
    line-height: 1.25;
    margin-bottom: 4px;
  }
  .contact-line {
    color: var(--ink-soft);
    font-size: 12px;
    line-height: 1.45;
  }

  /* Logo side */
  .card--logo {
    display: flex;
    align-items: center;
    justify-content: center;
  }
  .logo-name {
    color: var(--logo-grey);
    font-size: 38px;
    font-weight: 600;
    letter-spacing: 1px;
    margin-top: 40px;
  }
</style>
</head>
<body>
  <section class="card card--info" aria-label="Business card, information side">
    <div class="info__band">
      <p class="info__company">Larkmoor Continental<br>General Trading LLC</p>
    </div>
    <div class="info__details">
      <div class="person">
        <p class="person__name">Name Surname</p>
        <p class="person__position">Position</p>
        <p class="contact-line">0455 210 934</p>
        <p class="contact-line">0255 210 935</p>
      </div>
      <div class="address">
        <p class="contact-line">nlastname@larkmoor.com</p>
        <p class="contact-line">P.O. box Wrenfield Harbour</p>
      </div>
    </div>
  </section>

  <section class="card card--logo" aria-label="Business card, logo side">
    <p class="logo-name">Larkmoor Int.</p>
  </section>
</body>
</html>
```